Management Consulting needing a cool business card for client acquisition and networking

We are looking for a business card that is progressive and fresh that conveys innovation, forward thinking, and confidence. The business card is for a company based in Charlotte NC called, 'VELMORE CONSULTING GROUP LLC'. The company primarily works with banks, insurance, and brokerages to implement innovative solutions to help them streamline their operations, to more effectively manage risks, and to improve their customer relationships.

Target Market(s)

Typically meet with Chief Financial Officers, Chief Information Officers, Chief Operations Officer, Business Unit Leader. The target market are generally 40-55 years, male, white, master level education plus.

Industry/Entity Type

Progressive

Font styles to use
Serif
Other font styles liked:
• Calibri

Requirements
Should not have
• Designs that look too much like law firms or accounting companies. Too conservative

```html
<!DOCTYPE html>
<html lang="en">
<head>
<meta charset="utf-8">
<title>Velmore Consulting Group LLC — Business Card</title>
<link rel="stylesheet" href="https://fonts.googleapis.com/css2?family=Open+Sans:wght@400;600&family=Montserrat:wght@500&display=swap">
<style>
  :root {
    --backdrop: #8c8c8c;
    --card-black: #141414;
    --card-black-soft: #1d1d1d;
    --brand-red: #d92426;
    --text-white: #f2f2f2;
    --text-grey: #d8d8d8;
    --line-white: #e6e6e6;
  }
  * { margin: 0; padding: 0; box-sizing: border-box; }
  html, body { width: 1200px; height: 926px; overflow: hidden; }
  body {
    background: var(--backdrop);
    font-family: "Open Sans", "Calibri", sans-serif;
    position: relative;
  }
  .card {
    position: absolute;
    left: 250px;
    width: 700px;
    height: 400px;
    background: radial-gradient(ellipse at 60% 40%, var(--card-black-soft), var(--card-black) 70%);
    overflow: hidden;
    box-shadow: 0 6px 18px rgba(0,0,0,.35);
  }
  .card--front { top: 48px; }
  .card--back { top: 478px; }

  /* front */
  .band { position: absolute; left: 0; right: 0; bottom: 0; height: 52px; background: var(--brand-red); }
  .divider { position: absolute; left: 248px; width: 2px; background: var(--brand-red); }
  .divider--top { top: 0; height: 130px; }
  .divider--bottom { top: 150px; height: 182px; }

  .mark { position: absolute; left: 48px; top: 38px; display: flex; align-items: center; gap: 12px; }
  .mark-circle { width: 58px; height: 58px; border: 1.5px solid var(--line-white); border-radius: 50%; }
  .mark-name { font-size: 20px; font-weight: 600; color: var(--text-white); letter-spacing: 1px; }

  .person { position: absolute; left: 0; width: 240px; top: 170px; text-align: right; }
  .person-name { font-family: "Montserrat", sans-serif; font-weight: 500; font-size: 22px; color: var(--text-white); letter-spacing: 1px; }
  .person-title { font-family: "Montserrat", sans-serif; font-size: 10.5px; color: var(--brand-red); letter-spacing: 0.8px; margin-top: 3px; }

  .company { position: absolute; left: 282px; top: 74px; font-size: 25px; color: var(--text-white); }
  .contact { position: absolute; left: 282px; top: 196px; color: var(--text-grey); }
  .contact-address { font-size: 13px; margin-bottom: 6px; }
  .contact-line { font-size: 16px; line-height: 1.35; }
  .label { color: var(--brand-red); }
  .sep { color: var(--brand-red); margin: 0 6px; }

  /* back */
  .back-mark { position: absolute; left: 0; right: 0; top: 92px; display: flex; flex-direction: column; align-items: center; gap: 26px; }
  .back-circle { width: 150px; height: 150px; border: 1.5px solid var(--line-white); border-radius: 50%; }
  .back-name { font-size: 17px; color: var(--text-grey); letter-spacing: 5px; }
</style>
</head>
<body>
  <section class="card card--front" aria-label="Card front">
    <div class="divider divider--top"></div>
    <div class="divider divider--bottom"></div>
    <div class="mark">
      <div class="mark-circle"></div>
      <span class="mark-name">VELMORE</span>
    </div>
    <div class="person">
      <p class="person-name">MARCUS T. LORNE</p>
      <p class="person-title">CHIEF SOLUTIONS ARCHITECT</p>
    </div>
    <h1 class="company">Velmore Consulting Group LLC</h1>
    <div class="contact">
      <p class="contact-address">2715 Crestline rd., Suite 300, Charlotte, NC 28207</p>
      <p class="contact-line"><span class="label">o:</span> 704.555.0182<span class="sep">|</span><span class="label">c:</span> 704.555.0147</p>
      <p class="contact-line"><span class="label">e:</span> mlorne@velmoreconsulting.com</p>
    </div>
    <div class="band"></div>
  </section>

  <section class="card card--back" aria-label="Card back">
    <div class="back-mark">
      <div class="back-circle"></div>
      <p class="back-name">VELMORE CONSULTING GROUP LLC</p>
    </div>
  </section>
</body>
</html>
```